MODERN DESIGN BUSINESS CARDS FOR A CREDIT REPAIR COMPANY

Our goal is to have a modern yet professional business card for our credit repair company. Something that'll catch the eye of our clients. PLEASE BE CREATIVE. WE WOULD LIKE TO SEE HOW THIS WOULD LOOK WITH A WHITE AND BLACK BACK GROUND.

Contact Information for Business Card

THIS WILL BE A DOUBLE SIDED BUSINESS CARD, THE COLORS WE WOULD LIKE TO HAVE IS BLACK, BLUES AND WHITE

Colors
3277b5
33a6d7
ffffff

Requirements
Must have
• MUST HAVE OUR LOGO, BUSINESS PHONE # (482 )607-5731, EXAMPLESOCIAL LINK EXAMPLESOCIAL.TEST/VORMANTHCREDITSOLUTIONS, CALL US FOR YOUR FREE CONSULTATION
Nice to have
• ITEMS WE DELETE: LATE PAYMENTS, CHARGE-OFFS, REPOSESSIONS, HOSPITAL BILLS, STUDENT LOANS, FORECLOSURES, CHILD SUPPORT AND BANKRUPTCIES.

```html
<!DOCTYPE html>
<html lang="en">
<head>
<meta charset="utf-8">
<title>Vormanth Credit Solutions – Business Cards</title>
<link href="https://fonts.googleapis.com/css2?family=Montserrat:wght@500;700&family=Arimo:wght@400;700&display=swap" rel="stylesheet">
<style>
  :root {
    --page-bg: #2a2a2b;
    --card-bg: #0c0c0d;
    --brand-blue: #1f4f9c;
    --accent-blue: #3277b5;
    --text-light: #d6d6d8;
    --text-white: #ffffff;
    --rule-grey: #8a8a8e;
  }
  * { box-sizing: border-box; margin: 0; padding: 0; }
  html, body { width: 1200px; height: 900px; overflow: hidden; background: var(--page-bg); }
  .canvas {
    width: 1200px; height: 900px;
    display: flex; flex-direction: column; align-items: center; justify-content: center; gap: 40px;
  }
  .card {
    position: relative;
    width: 640px; height: 366px;
    background: var(--card-bg);
    box-shadow: 0 18px 40px rgba(0,0,0,.55);
    font-family: "Arimo", Arial, sans-serif;
    color: var(--text-light);
  }
  .brand {
    position: absolute; display: flex; align-items: center; gap: 14px;
  }
  .brand-mark {
    width: 62px; height: 62px; border-radius: 50%;
    border: 5px solid var(--text-light);
  }
  .brand-divider { width: 2px; height: 70px; background: var(--brand-blue); }
  .brand-name {
    font-family: "Montserrat", sans-serif; font-weight: 700; color: var(--brand-blue);
    font-size: 44px; line-height: 1; letter-spacing: 1px;
  }
  .brand-sub {
    font-family: "Montserrat", sans-serif; font-weight: 500; color: var(--text-white);
    font-size: 15px; letter-spacing: 6px; margin-top: 6px;
  }

  /* contact side */
  .card--contact .brand { left: 130px; top: 58px; }
  .consult { position: absolute; left: 0; right: 0; top: 184px; text-align: center; font-size: 20px; letter-spacing: .3px; }
  .phone { position: absolute; left: 0; right: 0; top: 216px; display: flex; justify-content: center; align-items: center; gap: 10px; font-size: 30px; color: var(--text-light); }
  .phone svg { width: 26px; height: 26px; }
  .social-rule { position: absolute; left: 60px; right: 60px; top: 278px; display: flex; align-items: center; gap: 12px; }
  .social-rule .line { flex: 1; height: 2px; background: var(--brand-blue); }
  .social-name { font-size: 14px; font-weight: 700; color: var(--accent-blue); letter-spacing: 1px; }
  .social-url { position: absolute; left: 0; right: 0; top: 304px; text-align: center; font-size: 18px; letter-spacing: .2px; }

  /* services side */
  .card--services .brand { left: 150px; top: 44px; }
  .services-rule { position: absolute; left: 230px; right: 40px; top: 150px; height: 1px; background: var(--rule-grey); }
  .services-title { position: absolute; left: 60px; top: 168px; font-size: 20px; font-weight: 700; color: var(--brand-blue); }
  .services-list { position: absolute; top: 204px; list-style: none; font-size: 20px; line-height: 27px; }
  .services-list li::before { content: ""; display: inline-block; width: 8px; height: 8px; border-radius: 50%; background: var(--brand-blue); margin-right: 9px; vertical-align: middle; }
  .services-list--a { left: 74px; }
  .services-list--b { left: 300px; }
  .certified-badge {
    position: absolute; right: 40px; top: 186px; width: 104px; height: 104px; border-radius: 50%;
    background: radial-gradient(circle, var(--accent-blue) 0 55%, var(--brand-blue) 56% 100%);
    border: 4px solid var(--text-white);
  }
</style>
</head>
<body>
<main class="canvas">
  <section class="card card--contact">
    <div class="brand">
      <div class="brand-mark"></div>
      <div class="brand-divider"></div>
      <div>
        <div class="brand-name">VORMANTH</div>
        <div class="brand-sub">CREDIT SOLUTIONS</div>
      </div>
    </div>
    <p class="consult">CALL US FOR YOUR FREE CONSULTATION</p>
    <p class="phone">
      <svg viewBox="0 0 24 24" aria-hidden="true"><path fill="#1f4f9c" d="M6.6 10.8a15.2 15.2 0 0 0 6.6 6.6l2.2-2.2c.3-.3.7-.4 1-.2 1.1.4 2.3.6 3.6.6.6 0 1 .4 1 1V20c0 .6-.4 1-1 1A17 17 0 0 1 3 4c0-.6.4-1 1-1h3.5c.6 0 1 .4 1 1 0 1.3.2 2.5.6 3.6.1.3 0 .7-.2 1z"/></svg>
      (482 )607-5731
    </p>
    <div class="social-rule">
      <span class="line"></span>
      <span class="social-name">EXAMPLESOCIAL</span>
      <span class="line"></span>
    </div>
    <p class="social-url">EXAMPLESOCIAL.TEST/VORMANTHCREDITSOLUTIONS</p>
  </section>

  <section class="card card--services">
    <div class="brand">
      <div class="brand-mark"></div>
      <div class="brand-divider"></div>
      <div>
        <div class="brand-name">VORMANTH</div>
        <div class="brand-sub">CREDIT SOLUTIONS</div>
      </div>
    </div>
    <div class="services-rule"></div>
    <p class="services-title">ITEMS WE DELETE:</p>
    <ul class="services-list services-list--a">
      <li>LATE PAYMENTS</li>
      <li>CHARGE-OFFS</li>
      <li>REPOSESSIONS</li>
      <li>HOSPITAL BILLS</li>
    </ul>
    <ul class="services-list services-list--b">
      <li>STUDENT LOANS</li>
      <li>FORECLOSURES</li>
      <li>CHILD SUPPORT</li>
      <li>BANKRUPTCIES</li>
    </ul>
    <div class="certified-badge" role="img" aria-label="Certification badge"></div>
  </section>
</main>
</body>
</html>
```